Business Card for IT company

I need a high tech looking business card using our logo. I prefer something clean and modern.

Target Market(s)

Buyers of IT hardware and software, IT Techies who are key influencers

Industry/Entity Type

Business

```html
<!DOCTYPE html>
<html lang="en">
<head>
<meta charset="utf-8">
<title>Voltline Consulting – Business Card</title>
<link href="https://fonts.googleapis.com/css2?family=Tinos&display=swap" rel="stylesheet">
<style>
  :root {
    --bg-light: #cfd0d2;
    --bg-dark: #8b8c90;
    --panel: #ffffff;
    --ink: #2f2f2f;
    --muted: #a6a6a6;
    --charcoal: #333333;
    --green-deep: #3a9a48;
    --green-bright: #8cc63f;
  }
  html, body {
    margin: 0;
    padding: 0;
    width: 1200px;
    height: 693px;
    overflow: hidden;
    background: var(--bg-dark);
  }
  .business-card {
    display: block;
    width: 1200px;
    height: 693px;
  }
  .card-text {
    font-family: "Tinos", "Times New Roman", serif;
  }
  .brand-name { fill: var(--ink); font-size: 124px; }
  .brand-tagline { fill: var(--ink); font-size: 26px; }
  .contact-label { fill: var(--ink); font-size: 38px; }
  .contact-value { fill: var(--muted); font-size: 38px; }
</style>
</head>
<body>
<svg class="business-card" viewBox="0 0 1063 614" preserveAspectRatio="none" xmlns="http://www.w3.org/2000/svg">
  <defs>
    <linearGradient id="backdrop-gradient" x1="0" y1="1" x2="1" y2="0">
      <stop offset="0" stop-color="var(--bg-light)"/>
      <stop offset="1" stop-color="var(--bg-dark)"/>
    </linearGradient>
    <linearGradient id="circuit-gradient" x1="0" y1="0" x2="1" y2="0">
      <stop offset="0" stop-color="var(--charcoal)"/>
      <stop offset="0.45" stop-color="var(--green-deep)"/>
      <stop offset="1" stop-color="var(--green-bright)"/>
    </linearGradient>
  </defs>

  <rect class="card-backdrop" width="1063" height="614" fill="url(#backdrop-gradient)"/>
  <rect class="card-panel" x="96" y="90" width="967" height="433" fill="var(--panel)"/>

  <g class="brand card-text">
    <text class="brand-name" x="128" y="270" textLength="350" lengthAdjust="spacingAndGlyphs">Voltline</text>
    <text class="brand-tagline" x="130" y="305" textLength="345" lengthAdjust="spacing">CONSULTING</text>
  </g>

  <g class="contact card-text">
    <text class="contact-label" x="718" y="205" text-anchor="end">Your Name</text>
    <text class="contact-value" x="729" y="205">Your Position</text>
    <text class="contact-label" x="718" y="257" text-anchor="end">Phone</text>
    <text class="contact-value" x="729" y="257">xxx.xxx.xxxx</text>
    <text class="contact-label" x="718" y="307" text-anchor="end">Email</text>
    <text class="contact-value" x="729" y="307">address@xx.com</text>
    <text class="contact-label" x="718" y="357" text-anchor="end">web</text>
    <text class="contact-value" x="729" y="357">xx.com</text>
  </g>

  <rect class="circuit-motif" role="img" aria-label="Circuit-board trace motif in charcoal and green running across the lower edge of the card"
        x="66" y="404" width="997" height="180" fill="url(#circuit-gradient)" opacity="0.85"/>
</svg>
</body>
</html>
```